Business Card Design

I give lessons and clinics for dressage riders
I would like the design to be an outline (with broad lines) of a dressage horse and rider with in background of whole card with print over top tan or parchment card with burgundy print

Industry/Entity Type

Business

Contact Information for Business Card

Ned Carrow
617-354-2790
Classical dressage training for the modern American
Clinics, lessons, training level -Prix St. George

Requirements
Must have
• broad lined outline of dressage horse and rider

```html
<!DOCTYPE html>
<html lang="en">
<head>
<meta charset="utf-8">
<title>Ned Carrow – Business Card</title>
<link rel="stylesheet" href="https://fonts.googleapis.com/css2?family=Marcellus&display=swap">
<style>
  :root {
    --backdrop: #ece7df;
    --card: #ffffff;
    --burgundy: #8a1f3c;
    --tan-soft: #f6e6d2;
    --tan-edge: #fbf3ea;
  }
  html, body {
    margin: 0;
    padding: 0;
    width: 1200px;
    height: 986px;
    overflow: hidden;
    background: var(--backdrop);
  }
  .business-card {
    position: absolute;
    left: 50px;
    top: 179px;
    width: 1100px;
    height: 628px;
    background: var(--card);
    box-shadow: 0 2px 8px rgba(0,0,0,0.12);
    overflow: hidden;
    font-family: "Marcellus", "Friz Quadrata", serif;
    color: var(--burgundy);
  }
  .horse-rider-art {
    position: absolute;
    left: 19%;
    top: 27%;
    width: 63%;
    height: 68%;
    border-radius: 45% 40% 30% 35%;
    background: radial-gradient(ellipse at 50% 50%, var(--tan-soft) 0%, var(--tan-edge) 60%, rgba(255,255,255,0) 100%);
  }
  .services {
    position: absolute;
    top: 46px;
    left: 0;
    width: 100%;
    margin: 0;
    text-align: center;
    font-size: 36px;
    line-height: 43px;
  }
  .services span { display: block; }
  .name {
    position: absolute;
    top: 300px;
    left: 0;
    width: 100%;
    margin: 0;
    text-align: center;
    font-size: 86px;
    line-height: 100px;
    font-weight: 400;
    -webkit-text-stroke: 2.5px var(--burgundy);
    letter-spacing: 1px;
  }
  .phone {
    position: absolute;
    top: 415px;
    left: 0;
    width: 100%;
    display: flex;
    justify-content: center;
    align-items: center;
    gap: 12px;
    font-size: 48px;
    line-height: 60px;
  }
  .phone-icon { width: 54px; height: 54px; }
</style>
</head>
<body>
  <main class="business-card">
    <div class="horse-rider-art" role="img" aria-label="Faint tan broad-lined outline of a dressage horse and rider in collected trot"></div>

    <p class="services">
      <span>Classical Dressage Training for the Modern</span>
      <span>American Clinics, Lessons,</span>
      <span>Training Level -Prix St. George</span>
    </p>

    <h1 class="name">Ned Carrow</h1>

    <div class="phone">
      <svg class="phone-icon" viewBox="0 0 54 54" aria-hidden="true">
        <circle cx="27" cy="27" r="20" fill="none" stroke="var(--burgundy)" stroke-width="4"/>
        <path d="M12 44 L44 10" stroke="var(--burgundy)" stroke-width="5" stroke-linecap="round"/>
        <path d="M17 32 q-2 -6 4 -10 l4 4 q-3 3 -1 6 q3 3 6 1 l4 4 q-4 6 -10 4 z" fill="var(--burgundy)"/>
      </svg>
      <span class="phone-number">617-354-2790</span>
    </div>
  </main>
</body>
</html>
```